Settlerhaus77.net flyer for window coverings

two sided 8 1/2 x 11 flyer featuring window coverings to send people to our website to shop for window coverings. Can use stock photos of blinds and shutters (wood toned blinds, white shutters, grey roller shades, white faux wood blinds). We don't sell draperies or drapery rods. We do sell other product like lighting and cabinet organization but we would like this flyer to focus on window coverings. We want to be a resource for new home buyers that need items to finish making their new house their home.

Target Market(s)

New home buyers

Industry/Entity Type

Real Estate

Font styles to use
Sans Serif

Requirements
Must have
• photos of window blinds and shades--photos have been added 3/31
• logo of settlerhaus77.net
• "Settlerhaus77.net - #1 - Cover your windows for: Privacy, Security, Energy Efficiency. We have all the styles to meet your needs and installation available!"
Should not have
• Pictures of towel bars

```html
<!DOCTYPE html>
<html lang="en">
<head>
<meta charset="utf-8">
<title>Settlerhaus77.net – Window Coverings Flyer</title>
<link href="https://fonts.googleapis.com/css2?family=Open+Sans:wght@400;600;700;800&family=Oswald:wght@500;600&display=swap" rel="stylesheet">
<style>
  :root{
    --red:#d3141c;
    --red-dark:#b00d14;
    --ink:#1f1f1f;
    --body:#3a3a3a;
    --paper:#f1f1f1;
    --band-grey:#c9c9c9;
    --footer:#3c3c3c;
    --stage:#e6e3de;
    --white:#ffffff;
    --social:#8d8d8d;
  }
  *{box-sizing:border-box;margin:0;padding:0}
  html,body{width:1200px;height:816px;overflow:hidden}
  body{background:var(--stage);font-family:"Open Sans",Arial,sans-serif}
  .canvas{position:relative;width:1200px;height:816px;overflow:hidden;background:var(--stage)}

  .flyer{position:absolute;top:123px;width:441px;height:570px;background:var(--paper);overflow:hidden;
    box-shadow:0 6px 14px rgba(0,0,0,.25)}
  .flyer--front{left:137px}
  .flyer--back{left:624px}

  .hero{position:absolute;left:0;top:0;width:441px;height:330px}

  .brand{position:absolute;right:20px;top:12px;text-align:right}
  .brand__row{display:flex;align-items:center;justify-content:flex-end;gap:6px}
  .brand__dot{width:30px;height:30px;border-radius:50%;background:var(--red)}
  .brand__name{font-weight:800;font-size:14px;color:var(--ink);letter-spacing:.2px}
  .brand__url{margin-top:6px;font-family:"Oswald",Arial,sans-serif;font-weight:600;font-size:15px;color:var(--red);letter-spacing:1.2px}

  .badge{position:absolute;left:41px;top:206px;width:100px;height:100px;border-radius:50%;background:var(--white);
    border:5px solid var(--red);box-shadow:0 2px 5px rgba(0,0,0,.3);display:flex;flex-direction:column;
    align-items:center;justify-content:center;text-align:center;line-height:1.05}
  .badge__off{font-weight:800;font-size:16px;color:var(--red)}
  .badge__line{font-weight:700;font-size:10px;color:var(--ink)}
  .badge__big{font-weight:700;font-size:16px;color:var(--ink)}
  .badge__code{font-weight:700;font-size:6.5px;color:var(--red);margin-top:1px}

  .headline{position:absolute;left:20px;top:312px}
  .headline__main{font-weight:700;font-size:20px;color:var(--ink);letter-spacing:.1px}
  .headline__sub{font-weight:400;font-size:15.5px;color:var(--red);letter-spacing:.3px;margin-top:-2px}

  .copy{position:absolute;left:21px;top:362px;width:215px;font-size:8px;line-height:1.35;color:var(--body)}
  .copy p{margin-bottom:6px}

  .photo-circle{position:absolute;border-radius:50%;border:4px solid var(--red);box-shadow:0 2px 4px rgba(0,0,0,.25)}
  .photo--wood-blinds{left:261px;top:315px;width:100px;height:100px;background:linear-gradient(160deg,#c77a42,#8a4a22)}
  .photo--living-room{left:328px;top:367px;width:86px;height:86px;background:linear-gradient(160deg,#e8e2d6,#a99c86)}
  .photo--roller-shade{left:261px;top:404px;width:80px;height:80px;background:linear-gradient(160deg,#9a4b33,#4a3a36)}

  .tagline{position:absolute;left:20px;top:283px;line-height:1.05}
  .tagline__top{font-weight:400;font-size:15px;color:var(--ink)}
  .tagline__mid{font-weight:700;font-size:17px;color:var(--ink)}
  .tagline__home{font-weight:700;font-size:27px;color:var(--red)}

  .photo--white-shutters{left:54px;top:350px;width:106px;height:106px;background:linear-gradient(160deg,#e9e4c9,#8c9a6a)}
  .photo--sunroom{left:143px;top:335px;width:130px;height:130px;z-index:2;background:linear-gradient(160deg,#eeeae2,#9c8e78)}
  .photo--faux-wood{left:279px;top:350px;width:106px;height:106px;background:linear-gradient(160deg,#d6dcd2,#6f8a7d)}

  .promo-bar{position:absolute;left:0;top:486px;width:441px;height:33px;background:linear-gradient(var(--red),var(--red-dark));
    color:var(--white);display:flex;align-items:center;justify-content:center}
  .promo-bar__text{font-weight:700;font-size:21px;letter-spacing:.4px}
  .promo-bar__url{font-family:"Oswald",Arial,sans-serif;font-weight:500;font-size:23px;letter-spacing:2px}

  .contact-bar{position:absolute;left:0;top:519px;width:441px;height:51px;background:var(--footer);color:var(--white)}
  .contact{position:absolute;left:25px;top:8px;font-size:11px;line-height:19px}
  .contact__row{display:flex;align-items:center;gap:8px}
  .contact__icon{width:13px;height:13px;border-radius:50%;background:var(--red);display:flex;align-items:center;justify-content:center}
  .contact__label{font-weight:700;font-size:11.5px}
  .social{position:absolute;left:331px;top:14px;display:flex;gap:9px}
  .social__dot{width:22px;height:22px;border-radius:50%;background:var(--social)}
</style>
</head>
<body>
<div class="canvas">

  <section class="flyer flyer--front">
    <svg class="hero" viewBox="0 0 441 330">
      <defs>
        <linearGradient id="frontRoom" x1="0" y1="0" x2="1" y2="1">
          <stop offset="0" stop-color="#e7e2d3"/>
          <stop offset=".55" stop-color="#d9d4c8"/>
          <stop offset="1" stop-color="#9f8a78"/>
        </linearGradient>
      </defs>
      <path d="M0,36 C140,22 290,62 441,88" fill="none" stroke="var(--band-grey)" stroke-width="6"/>
      <g role="img" aria-label="Bright living room with white plantation shutters on tall windows">
        <path d="M0,64 C140,52 290,86 441,112 L441,304 C300,270 150,244 0,262 Z" fill="url(#frontRoom)"/>
      </g>
      <path d="M0,44 C140,30 290,70 441,96 L441,112 C290,86 140,54 0,66 Z" fill="var(--red)"/>
      <path d="M0,256 C150,238 300,262 441,296" fill="none" stroke="var(--band-grey)" stroke-width="8"/>
      <path d="M0,262 C150,244 300,270 441,304 L441,316 C300,284 150,258 0,274 Z" fill="var(--red)"/>
    </svg>

    <div class="brand">
      <div class="brand__row"><span class="brand__dot"></span><span class="brand__name">SETTLERHAUS 77</span></div>
      <div class="brand__url">SETTLERHAUS77.NET</div>
    </div>

    <div class="badge">
      <span class="badge__off">10% OFF</span>
      <span class="badge__line">YOUR ENTIRE</span>
      <span class="badge__big">PURCHASE</span>
      <span class="badge__code">USE PROMO CODE</span>
      <span class="badge__code">SHHOME</span>
    </div>

    <div class="headline">
      <h1 class="headline__main">INSTALLED SOLUTIONS</h1>
      <p class="headline__sub">BLINDS • SHADES • SHUTTERS</p>
    </div>

    <div class="copy">
      <p>Settlerhaus77.net - #1 - Cover your windows for: Privacy, Security, Energy Efficiency. We have all the styles to meet your needs and installation available!</p>
      <p>Go to www.settlerhaus77.net and shop for your blinds, shades, shutters and more.</p>
      <p>During Checkout, enter promo code SHHOME and get a 10% discount on your entire purchase!</p>
    </div>

    <div class="photo-circle photo--wood-blinds" role="img" aria-label="Close-up of wood toned blinds"></div>
    <div class="photo-circle photo--roller-shade" role="img" aria-label="Brick wall window with a grey roller shade"></div>
    <div class="photo-circle photo--living-room" role="img" aria-label="Living room with white shutters"></div>

    <div class="promo-bar"><span class="promo-bar__text">FREE SHIPPING, NO MINIMUM!</span></div>

    <div class="contact-bar">
      <div class="contact">
        <div class="contact__row">
          <span class="contact__icon"><svg width="8" height="8" viewBox="0 0 10 10"><path d="M2 1 L4 1 L4.6 3 L3.4 3.8 C4 5 5 6 6.2 6.6 L7 5.4 L9 6 L9 8 C5 8.5 1.5 5 2 1 Z" fill="#fff"/></svg></span>
          <span><span class="contact__label">CALL US:</span> (555) 014-2290</span>
        </div>
        <div class="contact__row">
          <span class="contact__icon"><svg width="9" height="9" viewBox="0 0 10 10"><circle cx="5" cy="5" r="3.8" fill="none" stroke="#fff" stroke-width="1"/><path d="M1.2 5 H8.8 M5 1.2 C3 3.5 3 6.5 5 8.8 M5 1.2 C7 3.5 7 6.5 5 8.8" fill="none" stroke="#fff" stroke-width=".8"/></svg></span>
          <span>www.settlerhaus77.net</span>
        </div>
      </div>
      <div class="social"><span class="social__dot"></span><span class="social__dot"></span></div>
    </div>
  </section>

  <section class="flyer flyer--back">
    <svg class="hero" viewBox="0 0 441 330">
      <defs>
        <linearGradient id="backRoom" x1="0" y1="0" x2="1" y2="1">
          <stop offset="0" stop-color="#e4e4e2"/>
          <stop offset=".5" stop-color="#c9c9c6"/>
          <stop offset="1" stop-color="#6d6d6b"/>
        </linearGradient>
      </defs>
      <path d="M0,38 C140,24 290,64 441,92" fill="none" stroke="var(--band-grey)" stroke-width="6"/>
      <g role="img" aria-label="Modern living room with grey sofa and white faux wood blinds">
        <path d="M0,68 C140,56 290,90 441,116 L441,302 C300,266 150,246 0,258 Z" fill="url(#backRoom)"/>
      </g>
      <path d="M0,46 C140,32 290,74 441,100 L441,116 C290,90 140,58 0,70 Z" fill="var(--red)"/>
      <path d="M0,252 C150,240 300,258 441,294" fill="none" stroke="var(--band-grey)" stroke-width="8"/>
      <path d="M0,258 C150,246 300,266 441,302 L441,314 C300,280 150,260 0,270 Z" fill="var(--red)"/>
    </svg>

    <div class="brand">
      <div class="brand__row"><span class="brand__dot"></span><span class="brand__name">SETTLERHAUS 77</span></div>
      <div class="brand__url">SETTLERHAUS77.NET</div>
    </div>

    <div class="tagline">
      <p class="tagline__top">PUT THE FINISHING</p>
      <p class="tagline__mid">TOUCH ON YOUR</p>
      <h2 class="tagline__home">NEW HOME</h2>
    </div>

    <div class="photo-circle photo--white-shutters" role="img" aria-label="White shutter louvers with garden view"></div>
    <div class="photo-circle photo--faux-wood" role="img" aria-label="Close-up of white faux wood blind slats"></div>
    <div class="photo-circle photo--sunroom" role="img" aria-label="Sunroom seating with window shades"></div>

    <div class="promo-bar"><span class="promo-bar__url">SETTLERHAUS77.NET</span></div>

    <div class="contact-bar">
      <div class="contact">
        <div class="contact__row">
          <span class="contact__icon"><svg width="8" height="8" viewBox="0 0 10 10"><path d="M2 1 L4 1 L4.6 3 L3.4 3.8 C4 5 5 6 6.2 6.6 L7 5.4 L9 6 L9 8 C5 8.5 1.5 5 2 1 Z" fill="#fff"/></svg></span>
          <span><span class="contact__label">CALL US:</span> (555) 014-2290</span>
        </div>
        <div class="contact__row">
          <span class="contact__icon"><svg width="9" height="9" viewBox="0 0 10 10"><circle cx="5" cy="5" r="3.8" fill="none" stroke="#fff" stroke-width="1"/><path d="M1.2 5 H8.8 M5 1.2 C3 3.5 3 6.5 5 8.8 M5 1.2 C7 3.5 7 6.5 5 8.8" fill="none" stroke="#fff" stroke-width=".8"/></svg></span>
          <span>www.settlerhaus77.net</span>
        </div>
      </div>
      <div class="social"><span class="social__dot"></span><span class="social__dot"></span></div>
    </div>
  </section>

</div>
</body>
</html>
```